Label for flatbread

create an innovative and visually appealing label for flatbread packaging. The goal is to blend traditional bread-making heritage with a modern aesthetic that attracts consumers in retail environments while communicating freshness, quality, and authenticity.

To design a front-facing package label for flatbread that:
• Captures the essence of artisanal baking and cultural tradition.
• Stands out on shelves with strong visual appeal.
• You can use folk art to create the images on the label, elements like flatbread, wheat,
We want to print the label in a sticker and put it on bread bag, so consider that you are designing a label in a frame for instance 4 inch in 5 inch rectangular. We would like that the label has theme like the uploaded images (does not need to be similar to the uploaded images) these images give you a clue .

Target Market(s)

Groceries stores in Vancouver area Canada

Industry/Entity Type

Bakery

Font styles to use
Other font styles liked:
• feel free to choose your font yourself

Requirements
Must have
• Design the label to attract consumers and encourage them to choose this bread. Create an eye-catching label that entices consumers to try this bread. Make the label so appealing that consumers can’t resist picking up this bread.
Nice to have
• Clean, Illustration or icon of flatbread, Subtle grain (whole wheat!) or flour textures in the background to suggest craftsmanship, Made in Canada
Should not have
• we do not limit artists, use your imagination, do not put bread picture, the bread picture must be hand drawn

```html
<!DOCTYPE html>
<html lang="en">
<head>
<meta charset="UTF-8">
<title>Flat Bread Label</title>
<link rel="stylesheet" href="https://fonts.googleapis.com/css2?family=Alfa+Slab+One&family=Zilla+Slab:wght@500;700&display=swap">
<style>
  :root {
    --page: #ffffff;
    --label-tan: #e8d4b6;
    --panel-cream: #f6ece1;
    --frame-brown: #b48b66;
    --ink-brown: #6a3621;
    --text-brown: #5a3322;
    --bread-light: #f3cf6e;
    --bread-mid: #e2a846;
    --bread-deep: #c98a3a;
  }
  * { margin: 0; padding: 0; box-sizing: border-box; }
  html, body {
    width: 1200px;
    height: 858px;
    overflow: hidden;
    background: var(--page);
  }
  .canvas {
    position: relative;
    width: 1200px;
    height: 858px;
  }
  .label {
    position: absolute;
    left: 290px;
    top: 39px;
    width: 620px;
    height: 780px;
    background: var(--label-tan);
  }
  .label-frame {
    position: absolute;
    left: 0;
    top: 0;
    width: 620px;
    height: 600px;
  }
  .label-title {
    font-family: "Alfa Slab One", serif;
    font-size: 60px;
    fill: var(--ink-brown);
    letter-spacing: 1px;
  }
  .bread-illustration {
    position: absolute;
    left: 172px;
    top: 245px;
    width: 300px;
    height: 210px;
    border-radius: 50% 50% 46% 46% / 48% 48% 52% 52%;
    background: radial-gradient(ellipse at 45% 40%, var(--bread-light) 0%, var(--bread-mid) 65%, var(--bread-deep) 100%);
  }
  .label-info {
    position: absolute;
    left: 0;
    top: 590px;
    width: 620px;
    text-align: center;
    color: var(--text-brown);
    font-family: "Zilla Slab", serif;
  }
  .origin {
    font-size: 38px;
    font-weight: 700;
    letter-spacing: 0.5px;
    line-height: 50px;
  }
  .feature {
    font-size: 24px;
    font-weight: 500;
    line-height: 36px;
    display: flex;
    justify-content: center;
    align-items: center;
    gap: 8px;
  }
  .feature-list { margin-top: 12px; }
  .feature-icon {
    display: inline-block;
    width: 22px;
    height: 22px;
    border-radius: 4px;
    background: var(--bread-deep);
    opacity: 0.75;
  }
</style>
</head>
<body>
<main class="canvas">
  <section class="label">
    <svg class="label-frame" viewBox="0 0 620 600" xmlns="http://www.w3.org/2000/svg">
      <path d="M 90 62 Q 318 22 546 62 A 30 30 0 0 0 576 92 L 576 500 A 30 30 0 0 0 546 530 Q 318 556 90 530 A 30 30 0 0 0 60 500 L 60 92 A 30 30 0 0 0 90 62 Z"
            fill="var(--panel-cream)" stroke="var(--frame-brown)" stroke-width="4"/>
      <path d="M 90 62 Q 318 22 546 62 A 30 30 0 0 0 576 92 L 576 500 A 30 30 0 0 0 546 530 Q 318 556 90 530 A 30 30 0 0 0 60 500 L 60 92 A 30 30 0 0 0 90 62 Z"
            fill="none" stroke="var(--frame-brown)" stroke-width="2"
            transform="translate(318 296) scale(0.95) translate(-318 -296)"/>
      <path id="title-arc" d="M 110 215 Q 318 150 526 215" fill="none"/>
      <text class="label-title" text-anchor="middle">
        <textPath href="#title-arc" startOffset="50%">FLAT BREAD</textPath>
      </text>
    </svg>
    <div class="bread-illustration" role="img" aria-label="Hand-drawn illustration of two golden flatbreads stacked"></div>
    <div class="label-info">
      <p class="origin">Made in Canada</p>
      <div class="feature-list">
        <p class="feature">Whole Wheat <span class="feature-icon" role="img" aria-label="Wheat stalk icon"></span></p>
        <p class="feature">Baked locally <span class="feature-icon" role="img" aria-label="Steam icon"></span></p>
      </div>
    </div>
  </section>
</main>
</body>
</html>
```